Rollin’ Kites Copper Tide beer can design

We are not looking for a new logo, we want to use our current logo!! Current Logo is Attached. We want to incorporate our current logo into a full can design for our new non-alcoholic, THC infused Beer design. We cannot use animals or cartoons. We also can not say beer. We would like to use our main label found at www.rollinkites-example.com
Several ideas include having small images of beer cans and beer mugs all over the can as a background. Another idea is to make it freedom and liberty themed. We want to make sure people understand it is a beer, even though we can say beer on the can.

Target Market(s)

30-50 year olds

Industry/Entity Type

THC beverage

Logo Text

Rollin’ Kites Copper Tide

Colors
59FF00
82FF00
B8FF75
E3FFCB
F4FFEA

Requirements
Must have
• Full 12 oz beer can design
Should not have
• No word beer, do not need a new logo, need a can design

```html
<!DOCTYPE html>
<html lang="en">
<head>
<meta charset="utf-8">
<title>Rollin’ Kites Copper Tide – Can Wrap</title>
<link rel="stylesheet" href="https://fonts.googleapis.com/css2?family=Mulish:wght@700&family=Oswald:wght@700&family=Bebas+Neue&family=Anton&display=swap">
<style>
  :root {
    --gold: #ffc400;
    --gold-deep: #ffad00;
    --amber: #ff9a00;
    --green-dark: #1f6b12;
    --green: #3fae1f;
    --green-light: #b8ff75;
    --ink: #0b0b0b;
    --white: #ffffff;
    --grey: #9a9a9a;
  }
  * { margin: 0; padding: 0; box-sizing: border-box; }
  html, body { width: 1200px; height: 645px; overflow: hidden; background: var(--white); }
  .can-wrap { position: relative; width: 1200px; height: 645px; background: var(--white); }

  .strip { position: absolute; left: 5px; width: 1181px; background: var(--gold); }
  .strip--top { top: 12px; height: 18px; }
  .strip--bottom { top: 630px; height: 8px; }

  .band { position: absolute; left: 5px; width: 1181px; height: 49px; background: var(--gold); }
  .band--top { top: 39px; }
  .band--bottom { top: 571px; }
  .band__pattern {
    position: absolute; left: 0; right: 0; top: 8px; height: 35px;
    background: linear-gradient(180deg, var(--green-light) 0%, var(--green) 45%, var(--green-dark) 100%);
  }

  .main-panel {
    position: absolute; left: 5px; top: 98px; width: 1181px; height: 463px;
    background:
      radial-gradient(ellipse 420px 330px at 609px 200px,
        var(--gold) 0 38%, var(--gold-deep) 44%, var(--gold) 50%,
        var(--gold-deep) 62%, var(--gold) 68%, var(--amber) 80%, var(--gold) 88%),
      var(--gold);
  }

  .mission {
    position: absolute; left: 34px; top: 237px; width: 205px;
    font-family: "Mulish", sans-serif; font-weight: 700; font-size: 12px;
    line-height: 13.3px; color: var(--white);
  }

  .nutrition {
    position: absolute; left: 30px; top: 325px; width: 198px; height: 216px;
    background: var(--white);
  }
  .nutrition__label {
    position: absolute; top: 42px; left: 0; right: 0; text-align: center;
    font-family: "Mulish", sans-serif; font-weight: 700; font-size: 12px; color: var(--ink);
  }

  .upc {
    position: absolute; left: 1055px; top: 325px; width: 114px; height: 215px;
    background: var(--white); overflow: hidden;
  }
  .upc__label {
    position: absolute; left: 50%; top: 50%;
    transform: translate(-50%, -50%) rotate(90deg);
    font-family: "Anton", sans-serif; font-size: 46px; letter-spacing: 1px;
    color: var(--grey); white-space: nowrap;
  }

  .brand {
    position: absolute; left: 384px; top: 130px; width: 460px; height: 340px;
    text-align: center;
  }
  .brand__disc {
    position: absolute; left: 50%; top: 10px; width: 150px; height: 150px;
    transform: translateX(-50%); border-radius: 50%; background: var(--green-dark);
  }
  .brand__name {
    position: absolute; left: 0; right: 0; top: 190px;
    font-family: "Oswald", sans-serif; font-weight: 700; font-size: 58px;
    line-height: 1; color: var(--ink); text-transform: uppercase;
  }

  .product-name {
    position: absolute; left: 384px; top: 482px; width: 460px; text-align: center;
    font-family: "Bebas Neue", sans-serif; font-size: 66px; line-height: 1;
    color: var(--white); letter-spacing: 1px;
  }
</style>
</head>
<body>
  <div class="can-wrap">
    <div class="strip strip--top"></div>

    <div class="band band--top">
      <div class="band__pattern" role="img" aria-label="Green faceted triangle pattern band"></div>
    </div>

    <div class="main-panel" role="img" aria-label="Golden background with soft orange ripple rings"></div>

    <p class="mission">Our mission is to create premium cannabis beverages that bridge the gap from recreational alcohol to low dose THC. Cocktails can be delicious, highly relaxing, and fun without alcohol</p>

    <div class="nutrition">
      <p class="nutrition__label">NUTRITION INFO</p>
    </div>

    <div class="brand">
      <div class="brand__disc"></div>
      <p class="brand__name">Rollin’ Kites</p>
    </div>

    <p class="product-name">COPPER TIDE</p>

    <div class="upc">
      <span class="upc__label">UPC CODE</span>
    </div>

    <div class="band band--bottom">
      <div class="band__pattern" role="img" aria-label="Green faceted triangle pattern band"></div>
    </div>

    <div class="strip strip--bottom"></div>
  </div>
</body>
</html>
```